New Stationery New Logo for KT Mouldings Limited

We have a new logo and now want new stationary to go with it

This will be

Letterhead
Compliments Slip
Business Cards

Company details are
KT Mouldings Limited
Brindle Row, Rugby, Warwickshire, CV34 7HX, UK
Telephone : +44(0)1788 930467
Fax: +44(0)1788 918723
Email: sales@ktmouldings.example
Web: www.ktmouldings.example

Target Market(s)

Engineering / Metal Stamping

Industry/Entity Type

Manufacture

Contact Information for Business Card

Neil Garbutt
Business Development Manager
KT Mouldings Limited
Brindle Row
Rugby
Warwickshire
CV34 7HX, UK

T: +44(0)1788 930467
F: +44(0)1788 918723
E: sales@ktmouldings.example
W: www.ktmouldings.example

Font styles to use
Sans Serif

Colors
33a6d7
0555a3
3176b5
85cae6
85acd3

Requirements
Must have
• Logo

```html
<!DOCTYPE html>
<html lang="en">
<head>
<meta charset="utf-8">
<title>KT Mouldings Limited – Stationery</title>
<link rel="stylesheet" href="https://fonts.googleapis.com/css2?family=Open+Sans:ital,wght@0,400;0,600;1,400&display=swap">
<style>
  :root {
    --brand-blue: #0d4c96;
    --stripe-blue: #1a5aa8;
    --accent-blue: #3176b5;
    --ink: #1f2a3d;
    --paper: #ffffff;
    --slip-paper: #f4f5f7;
    --backdrop: #e9eaec;
  }
  * { box-sizing: border-box; margin: 0; padding: 0; }
  html, body { width: 1200px; height: 867px; overflow: hidden; }
  body { background: var(--backdrop); font-family: "Open Sans", Arial, sans-serif; color: var(--ink); }
  .canvas { position: relative; width: 1200px; height: 867px; overflow: hidden; }

  .sheet { position: absolute; overflow: hidden; box-shadow: 0 2px 6px rgba(0,0,0,.18); }
  .band { position: absolute; background: var(--brand-blue); }
  .stripes-v, .stripes-h { position: absolute; display: flex; gap: 3px; }
  .stripes-v span { width: 3px; height: 100%; background: var(--stripe-blue); }
  .stripes-h { flex-direction: column; }
  .stripes-h span { height: 3px; width: 100%; background: var(--stripe-blue); }

  .wordmark { position: absolute; display: flex; align-items: center; gap: 8px;
    font-weight: 600; color: var(--ink); letter-spacing: .28em; white-space: nowrap; }
  .wordmark .dot { border-radius: 50%; background: var(--brand-blue); flex: none; }

  /* Compliments slip */
  .comp-slip { left: 40px; top: 40px; width: 540px; height: 255px; background: var(--slip-paper); }
  .comp-slip .band { left: 0; top: 0; width: 304px; height: 100%; }
  .comp-slip .stripes-v { left: 307px; top: 0; height: 100%; }
  .comp-slip .title { position: absolute; left: 36px; top: 16px; color: #fff; font-size: 17px; }
  .comp-slip .note-box { position: absolute; left: 62px; top: 47px; width: 261px; height: 164px; background: var(--paper); }
  .comp-slip .wordmark { left: 326px; width: 214px; justify-content: center; top: 92px; font-size: 13px; }
  .comp-slip .wordmark .dot { width: 10px; height: 10px; }
  .comp-slip .details { position: absolute; left: 326px; width: 214px; top: 203px; text-align: center; font-size: 7.5px; line-height: 11px; }
  .details .co-name { color: var(--accent-blue); font-size: 10px; }
  .details .label { color: var(--accent-blue); }

  /* Letterhead */
  .letterhead { left: 610px; top: 40px; width: 550px; height: 778px; background: var(--paper); }
  .letterhead .wordmark { left: 40px; top: 46px; font-size: 20px; }
  .letterhead .wordmark .dot { width: 14px; height: 14px; }
  .letterhead .contact { position: absolute; right: 22px; top: 94px; text-align: right; font-size: 8.5px; line-height: 12px; color: var(--brand-blue); }
  .letterhead .band-side { left: 412px; top: 160px; width: 138px; height: 618px; }
  .letterhead .band-foot { left: 120px; top: 690px; width: 430px; height: 88px; }
  .letterhead .stripes-h { left: 412px; top: 140px; width: 138px; }
  .letterhead .stripes-v { left: 100px; top: 690px; height: 88px; }
  .letterhead .address { position: absolute; left: 22px; top: 638px; font-size: 10px; line-height: 14px; }
  .letterhead .address .co-name { color: var(--accent-blue); font-style: italic; font-size: 11px; }
  .letterhead .web { position: absolute; left: 150px; top: 724px; color: #fff; font-size: 13px; }

  /* Business card front */
  .card-front { left: 140px; top: 335px; width: 340px; height: 210px; background: var(--paper); }
  .card-front .wordmark { left: 22px; top: 40px; font-size: 14px; }
  .card-front .wordmark .dot { width: 10px; height: 10px; }
  .card-front .band-side { left: 275px; top: 30px; width: 65px; height: 180px; }
  .card-front .band-foot { left: 100px; top: 170px; width: 240px; height: 40px; }
  .card-front .stripes-h { left: 275px; top: 14px; width: 65px; }
  .card-front .stripes-v { left: 82px; top: 170px; height: 40px; }
  .card-front .web { position: absolute; left: 118px; top: 183px; color: #fff; font-size: 9px; display: flex; align-items: center; gap: 5px; }
  .icon-sq { display: inline-block; width: 7px; height: 7px; background: #fff; flex: none; }

  /* Business card back */
  .card-back { left: 140px; top: 590px; width: 340px; height: 210px; background: var(--paper); }
  .card-back .wordmark { left: 18px; top: 30px; font-size: 11px; }
  .card-back .wordmark .dot { width: 8px; height: 8px; }
  .card-back .web { position: absolute; left: 18px; top: 182px; font-size: 8px; }
  .card-back .band-side { left: 196px; top: 0; width: 144px; height: 210px; }
  .card-back .id-panel { position: absolute; left: 206px; top: 14px; width: 124px; height: 124px; background: var(--paper); padding: 9px 8px; }
  .id-panel .name { font-size: 9.5px; font-weight: 600; color: var(--ink); }
  .id-panel .role { font-size: 6.5px; color: var(--accent-blue); margin-bottom: 8px; white-space: nowrap; }
  .id-panel ul { list-style: none; font-size: 6.5px; line-height: 12px; }
  .id-panel li { display: flex; align-items: center; gap: 4px; white-space: nowrap; }
  .id-panel li .icon-sq { background: var(--brand-blue); }
  .card-back .address { position: absolute; left: 208px; top: 150px; color: #fff; font-size: 7.5px; line-height: 11px; }
</style>
</head>
<body>
<main class="canvas">

  <section class="sheet comp-slip" aria-label="Compliments slip">
    <div class="band"></div>
    <div class="stripes-v"><span></span><span></span><span></span></div>
    <p class="title">With Compliments...</p>
    <div class="note-box"></div>
    <div class="wordmark"><span class="dot"></span>KT MOULDINGS</div>
    <div class="details">
      <p class="co-name">KT Mouldings Limited</p>
      <p>Brindle Row, Rugby, Warwickshire, CV34 7HX, UK</p>
      <p><span class="label">Email</span> - sales@ktmouldings.example</p>
      <p><span class="label">Tel.</span> - +44(0)1788 930467 &nbsp;&nbsp; <span class="label">Fax.</span>- +44(0)1788 918723</p>
    </div>
  </section>

  <section class="sheet letterhead" aria-label="Letterhead">
    <div class="wordmark"><span class="dot"></span>KT MOULDINGS</div>
    <div class="contact">
      <p>Email - sales@ktmouldings.example</p>
      <p>Tel. - +44(0)1788 930467</p>
      <p>Fax. - +44(0)1788 918723</p>
    </div>
    <div class="stripes-h"><span></span><span></span><span></span></div>
    <div class="band band-side"></div>
    <div class="stripes-v"><span></span><span></span><span></span></div>
    <div class="band band-foot"></div>
    <div class="address">
      <p class="co-name">KT Mouldings Limited</p>
      <p>Brindle Row, Rugby, Warwickshire, CV34 7HX, UK</p>
    </div>
    <p class="web">www.ktmouldings.example</p>
  </section>

  <section class="sheet card-front" aria-label="Business card, front">
    <div class="wordmark"><span class="dot"></span>KT MOULDINGS</div>
    <div class="stripes-h"><span></span><span></span><span></span></div>
    <div class="band band-side"></div>
    <div class="stripes-v"><span></span><span></span><span></span></div>
    <div class="band band-foot"></div>
    <p class="web"><span class="icon-sq"></span>www.ktmouldings.example</p>
  </section>

  <section class="sheet card-back" aria-label="Business card, back">
    <div class="wordmark"><span class="dot"></span>KT MOULDINGS</div>
    <p class="web">www.ktmouldings.example</p>
    <div class="band band-side"></div>
    <div class="id-panel">
      <p class="name">Neil Garbutt</p>
      <p class="role">Business Development Manager</p>
      <ul>
        <li><span class="icon-sq"></span>+44(0)1788 930467</li>
        <li><span class="icon-sq"></span>+44(0)1788 918723</li>
        <li><span class="icon-sq"></span>sales@ktmouldings.example</li>
        <li><span class="icon-sq"></span>www.ktmouldings.example</li>
      </ul>
    </div>
    <div class="address">
      <p>Brindle Row, Rugby,</p>
      <p>Warwickshire, CV34 7HX, UK</p>
    </div>
  </section>

</main>
</body>
</html>
```